We are seeking two label designs for our premium pecan snack brand, MORVELO. MORVELO is known for its innovative pecan snacks, specifically a healthy and exotic blend of pecans, expertly salted, and infused with unique chili flavors. Our snacks are packaged in stand-up pouch bags, and we are looking for label designs product sizes - 5 oz. ( Size: 14 x 20 cm / 5.5 x 7.8 inches / Max Capacity: 16.2 oz)

Background Information:
MORVELO is a brand committed to offering a delightful snacking experience that combines the natural richness of pecans with the bold and exotic kick of carefully selected chilies. Our snacks cater to health-conscious consumers who appreciate the fusion of premium quality, unique flavors, and nutritional goodness.

Target Market(s)

Event Attendees (Entertainment Industry), Health-Conscious Consumers

Industry/Entity Type

Entertainment (sports events, arenas, stadiums, etc)

Font styles to use
Other font styles liked:
• Brother1816 Printed

Colors

Designer to choose colors to be used in the design.

Requirements
Must have
• Nutrition Fact (attached) , TRANSPARENT PART LIKE A WINDOW TO DISPLAY THE PRODUCT

```html
<!DOCTYPE html>
<html lang="en">
<head>
<meta charset="utf-8">
<title>MORVELO Spice Roasted Pecans – 5 oz Pouch Label</title>
<link rel="stylesheet" href="https://fonts.googleapis.com/css2?family=Josefin+Sans:wght@300;700&family=Montserrat:wght@700&display=swap">
<style>
  :root {
    --page: #ffffff;
    --pouch-dark: #0b0b0b;
    --pouch-mid: #5a5a5a;
    --orange: #f26a3a;
    --orange-light: #f7a68a;
    --white: #ffffff;
    --nut-dark: #6b2a10;
    --nut-light: #d98a45;
  }
  html, body {
    margin: 0;
    padding: 0;
    width: 1200px;
    height: 1200px;
    overflow: hidden;
    background: var(--page);
  }
  .canvas {
    position: relative;
    width: 1200px;
    height: 1200px;
  }
  .pouch-art {
    position: absolute;
    inset: 0;
  }
  .brand-name {
    position: absolute;
    left: 493px;
    width: 214px;
    top: 318px;
    margin: 0;
    text-align: center;
    font-family: "Josefin Sans", sans-serif;
    font-weight: 700;
    font-size: 33px;
    letter-spacing: 1px;
    color: var(--white);
    line-height: 1;
    white-space: nowrap;
  }
  .product-title {
    margin: 0;
    font-family: "Josefin Sans", sans-serif;
    font-weight: 700;
    line-height: 1;
    color: var(--white);
  }
  .product-title span {
    position: absolute;
    left: 0;
    width: 1200px;
    text-align: center;
    white-space: nowrap;
  }
  .title-spice { top: 470px; font-size: 134px; letter-spacing: 1px; }
  .title-roasted { top: 596px; font-size: 74px; color: var(--orange); }
  .title-pecans { top: 670px; font-size: 88px; }
  .tagline {
    position: absolute;
    left: 0;
    width: 1200px;
    top: 772px;
    margin: 0;
    text-align: center;
    font-family: "Josefin Sans", sans-serif;
    font-weight: 300;
    font-size: 37px;
    line-height: 47px;
    color: var(--orange);
  }
  .net-weight {
    position: absolute;
    left: 0;
    width: 1200px;
    top: 996px;
    margin: 0;
    text-align: center;
    font-family: "Montserrat", sans-serif;
    font-weight: 700;
    font-size: 16px;
    color: var(--white);
  }
</style>
</head>
<body>
<div class="canvas">
  <svg class="pouch-art" width="1200" height="1200" viewBox="0 0 1200 1200" xmlns="http://www.w3.org/2000/svg">
    <defs>
      <radialGradient id="pouchSheen" cx="0.5" cy="0.45" r="0.6">
        <stop offset="0" stop-color="#5a5a5a"/>
        <stop offset="0.55" stop-color="#1c1c1c"/>
        <stop offset="1" stop-color="#0b0b0b"/>
      </radialGradient>
      <linearGradient id="bannerFill" x1="0" y1="0" x2="0" y2="1">
        <stop offset="0" stop-color="#f26a3a"/>
        <stop offset="1" stop-color="#f7a68a"/>
      </linearGradient>
      <linearGradient id="nutFill" x1="0" y1="0" x2="1" y2="1">
        <stop offset="0" stop-color="#d98a45"/>
        <stop offset="0.5" stop-color="#a24a1c"/>
        <stop offset="1" stop-color="#6b2a10"/>
      </linearGradient>
    </defs>

    <rect class="pouch-body" x="312" y="120" width="580" height="934" fill="url(#pouchSheen)"/>
    <rect class="seal-top" x="312" y="120" width="580" height="150" fill="#0f0f0f" opacity="0.75"/>
    <line class="zip-line" x1="312" y1="272" x2="892" y2="272" stroke="#3a3a3a" stroke-width="2"/>

    <path class="brand-banner" d="M481 120 H719 V407 L600 448 L481 407 Z" fill="url(#bannerFill)"/>
    <path class="brand-banner-frame" d="M493 120 V399 L600 436 L707 399 V120" fill="none" stroke="#ffffff" stroke-width="2"/>

    <path class="product-window" role="img" aria-label="Clear window showing spice roasted pecans"
          d="M428 880 C436 874 446 880 460 886 C520 900 600 892 680 888 C730 885 762 880 782 872 C776 902 752 924 712 934 C650 950 600 960 540 962 C490 964 452 952 438 930 C430 912 422 896 428 880 Z"
          fill="url(#nutFill)"/>
  </svg>

  <p class="brand-name">MORVELO</p>

  <h1 class="product-title">
    <span class="title-spice">SPICE</span>
    <span class="title-roasted">ROASTED</span>
    <span class="title-pecans">PECANS</span>
  </h1>

  <p class="tagline">WITH CAREFULLY<br>SELECTED CHILIES</p>

  <p class="net-weight">NET WT 5 OZ (142g)</p>
</div>
</body>
</html>
```